Verdant Loop Advisors, LLC

I am looking for a simple, clear layout with my logo prominent and embossed, on the best quality card stock available. I would like the business name and phone number included on the card as well......I dont want my name anywhere on the card and I would like my logo embossed on the card......something simple with a white back......open to designs as long as they go along with recycling symbols and green type stuff.....The address, website, cell number, fax number, and email are listed below

5374 Tillbury Fenwood Road
Glenhollow, MD 20999

c. 240.555.0143 f. 240.555.0187
e. sales@verdantloopadvisors.example
w. www.verdantloopadvisors.example

Industry/Entity Type

Recycling

```html
<!DOCTYPE html>
<html lang="en">
<head>
<meta charset="utf-8">
<title>Verdant Loop Advisors, LLC – Business Card</title>
<link rel="stylesheet" href="https://fonts.googleapis.com/css2?family=Michroma&display=swap">
<style>
  :root {
    --backdrop: #1f2022;
    --card: #4a4b4d;
    --card-edge: #3f4042;
    --emboss: #3a3b3d;
    --mark-tone: #525355;
    --ink: #e6e6e6;
    --rule: #9a9b9d;
  }
  * { margin: 0; padding: 0; box-sizing: border-box; }
  html, body {
    width: 1200px;
    height: 800px;
    overflow: hidden;
    background: var(--backdrop);
  }
  .canvas {
    position: relative;
    width: 1200px;
    height: 800px;
    display: flex;
    align-items: center;
    justify-content: center;
  }
  .business-card {
    position: relative;
    width: 900px;
    height: 514px;
    background: var(--card);
    border: 1px solid var(--card-edge);
    overflow: hidden;
    font-family: "Michroma", sans-serif;
  }
  .background-mark {
    position: absolute;
    left: 150px;
    top: -40px;
    width: 500px;
    height: 500px;
  }
  .brand {
    position: absolute;
    left: 80px;
    top: 96px;
    display: flex;
    align-items: flex-start;
    gap: 22px;
    color: var(--emboss);
  }
  .brand-square {
    width: 72px;
    height: 72px;
    background: var(--emboss);
    margin-top: 6px;
  }
  .brand-name {
    display: flex;
    flex-direction: column;
    font-weight: 400;
  }
  .brand-name-main {
    font-size: 58px;
    line-height: 1;
    letter-spacing: 1px;
  }
  .brand-name-sub {
    font-size: 22px;
    line-height: 1;
    letter-spacing: 17px;
    margin-top: 10px;
    text-align: right;
  }
  .contact {
    position: absolute;
    color: var(--ink);
    font-size: 16px;
    font-style: normal;
    line-height: 1.45;
    letter-spacing: 0.5px;
    white-space: nowrap;
  }
  .contact-address {
    right: 56px;
    top: 300px;
    text-align: right;
  }
  .contact-online {
    left: 56px;
    top: 356px;
  }
  .contact-phones {
    right: 56px;
    top: 356px;
    text-align: right;
  }
  .divider {
    position: absolute;
    left: 630px;
    top: 356px;
    width: 1px;
    height: 48px;
    background: var(--rule);
  }
</style>
</head>
<body>
  <main class="canvas">
    <section class="business-card" aria-label="Verdant Loop Advisors business card">
      <svg class="background-mark" role="img" aria-label="Faint large recycling mark decoration area" viewBox="0 0 500 500">
        <circle cx="250" cy="250" r="240" fill="var(--mark-tone)" opacity="0.45"/>
      </svg>

      <div class="brand">
        <span class="brand-square" aria-hidden="true"></span>
        <h1 class="brand-name">
          <span class="brand-name-main">VERDANT LOOP</span>
          <span class="brand-name-sub">ADVISORS LLC</span>
        </h1>
      </div>

      <address class="contact contact-address">
        5374 TILLBURY FENWOOD ROAD<br>
        GLENHOLLOW, MD 20999
      </address>

      <p class="contact contact-online">
        SALES@VERDANTLOOPADVISORS.EXAMPLE<br>
        WWW.VERDANTLOOPADVISORS.EXAMPLE
      </p>

      <span class="divider" aria-hidden="true"></span>

      <p class="contact contact-phones">
        240.555.0143 : C<br>
        240.555.0187 : F
      </p>
    </section>
  </main>
</body>
</html>
```